A-Stand Directional Sign Design

Objective:
We need a professional graphic design for an A-Stand sign that will guide customers arriving in our parking lot to our office. The design should be visually clear, welcoming, and aligned with our brand identity.
REQUIREMENTS:
Two versions of the design:
- One with an arrow pointing left
- One with an arrow pointing right
(This allows us to place the A-Stand anywhere and flip the graphic as needed.)
DIMENSIONS:
- Viewable Area: 30" x 40"
BRAND ALIGNMENT:
- Colors, fonts, and overall style should match our website: www.skornabel.com
- Clean, modern, and professional look consistent with our aviation/tourism brand
CONTENT:
- Clear directional arrow (left or right depending on version)
- Text: “Office Entrance” or similar concise wording (designers may propose alternatives if they improve clarity)
READABILITY:
- Bold, high-contrast design for visibility from a distance
- Simple layout that avoids clutter
DELIVERABLES:
- Final artwork in print-ready format (PDF preferred)
- Two versions: Arrow Left and Arrow Right
DESIGN GOAL:
Ensure customers can easily find our office upon arrival, while reinforcing skorNABEL’s professional and welcoming brand image.
Target Market(s)
Tourism

```html
<!DOCTYPE html>
<html lang="en">
<head>
<meta charset="utf-8">
<title>skorNABEL A-Stand Directional Signs</title>
<link href="https://fonts.googleapis.com/css2?family=Montserrat:wght@600;700;800&display=swap" rel="stylesheet">
<style>
  :root {
    --brand-blue: #2b78b8;
    --band-blue: #86a9d6;
    --paper: #ffffff;
    --stage: #3b3b3b;
    --photo-warm: #d9c6b0;
    --photo-light: #f2efec;
  }
  html, body {
    margin: 0;
    padding: 0;
    width: 1200px;
    height: 804px;
    overflow: hidden;
    background: var(--stage);
  }
  .canvas {
    position: relative;
    width: 1200px;
    height: 804px;
  }
  .sign {
    position: absolute;
    top: 86px;
    width: 484px;
    height: 643px;
    display: block;
  }
  .sign--right-arrow { left: 102px; }
  .sign--left-arrow { left: 614px; }
  .sign-title {
    font-family: 'Montserrat', sans-serif;
    font-weight: 800;
    font-size: 80px;
    fill: var(--paper);
    letter-spacing: -1px;
  }
  .brand-name {
    font-family: 'Montserrat', sans-serif;
    font-weight: 700;
    font-size: 40px;
    fill: var(--brand-blue);
  }
</style>
</head>
<body>
<main class="canvas">

  <!-- Arrow pointing right -->
  <svg class="sign sign--right-arrow" viewBox="0 0 650 864" aria-label="Office entrance sign, arrow pointing right">
    <defs>
      <linearGradient id="photoFadeRight" x1="0" y1="0" x2="1" y2="0">
        <stop offset="0" stop-color="var(--photo-light)" stop-opacity="0"/>
        <stop offset="0.35" stop-color="var(--photo-light)"/>
        <stop offset="1" stop-color="var(--photo-warm)"/>
      </linearGradient>
    </defs>
    <rect class="sign-paper" width="650" height="864" fill="var(--paper)"/>
    <rect class="photo-area" x="250" y="470" width="400" height="394" fill="url(#photoFadeRight)" role="img" aria-label="Photo of a passenger wearing an aviation headset looking out of a helicopter window"/>
    <path class="top-band" d="M0,0 H650 V480 Q325,610 0,480 Z" fill="var(--brand-blue)"/>
    <path class="top-band-accent" d="M0,480 Q325,610 650,480 V500 Q325,650 0,510 Z" fill="var(--band-blue)"/>
    <path class="corner-accent" d="M330,864 Q470,760 650,735 V760 Q470,790 380,864 Z" fill="var(--band-blue)"/>
    <path class="corner-band" d="M380,864 Q470,790 650,760 V864 Z" fill="var(--brand-blue)"/>
    <path class="direction-arrow" d="M93,150 H343 L291,62 L556,170 L291,278 L343,190 H93 Z" fill="var(--paper)"/>
    <text class="sign-title" x="326" y="372" text-anchor="middle">OFFICE</text>
    <text class="sign-title" x="326" y="452" text-anchor="middle">ENTRANCE</text>
    <text class="brand-name" x="180" y="788" text-anchor="middle">skorNABEL.com</text>
  </svg>

  <!-- Arrow pointing left -->
  <svg class="sign sign--left-arrow" viewBox="0 0 650 864" aria-label="Office entrance sign, arrow pointing left">
    <defs>
      <linearGradient id="photoFadeLeft" x1="1" y1="0" x2="0" y2="0">
        <stop offset="0" stop-color="var(--photo-light)" stop-opacity="0"/>
        <stop offset="0.35" stop-color="var(--photo-light)"/>
        <stop offset="1" stop-color="var(--photo-warm)"/>
      </linearGradient>
    </defs>
    <rect class="sign-paper" width="650" height="864" fill="var(--paper)"/>
    <rect class="photo-area" x="0" y="470" width="420" height="394" fill="url(#photoFadeLeft)" role="img" aria-label="Photo of a smiling couple wearing aviation headsets inside a helicopter cabin"/>
    <g transform="translate(650,0) scale(-1,1)">
      <path class="top-band" d="M0,0 H650 V480 Q325,610 0,480 Z" fill="var(--brand-blue)"/>
      <path class="top-band-accent" d="M0,480 Q325,610 650,480 V500 Q325,650 0,510 Z" fill="var(--band-blue)"/>
      <path class="corner-accent" d="M330,864 Q470,760 650,735 V760 Q470,790 380,864 Z" fill="var(--band-blue)"/>
      <path class="corner-band" d="M380,864 Q470,790 650,760 V864 Z" fill="var(--brand-blue)"/>
      <path class="direction-arrow" d="M93,150 H343 L291,62 L556,170 L291,278 L343,190 H93 Z" fill="var(--paper)"/>
    </g>
    <text class="sign-title" x="326" y="372" text-anchor="middle">OFFICE</text>
    <text class="sign-title" x="326" y="452" text-anchor="middle">ENTRANCE</text>
    <text class="brand-name" x="470" y="788" text-anchor="middle">skorNABEL.com</text>
  </svg>

</main>
</body>
</html>
```